Kenwick Falcons FC Website

We are looking to develop a new website for Kenwick FC. Kenwick FC has now joined with Kenwick Falcons FC and we are looking at a website that can work for both clubs. Kenwick FC play in a local park football competition while kenwick Falcons are a Semi Professional team that plays in the Coastal Premier Division Competition. What we are after is two separate website off the one platform. I have attached both team logos for you to visualise. Also you can look at the existing kenwick website www.kenwickfc-demo.com.au. We are looking for a huge improvement in the website and it will be imperative we have links to sponsors and the sponsors can get regular visuals. Weare looking to move this club forward and have a very professional website that can communicate clearly with the community.

Hi All,

Please remember that the website is to represent two clubs;
1. Kenwick Falcons FC (Competes in Semi Professional League)
2. Kenwick FC (Compete in HBJCA League which is a lower level)

Further to this the Kenwick Falcons FC page will require a player profile page which will show photos of each player and a little bio on each.

Thanks

Reason: Would like to spend more time review existing and new designs

```html
<!DOCTYPE html>
<html lang="en">
<head>
<meta charset="utf-8">
<title>Kenwick FC</title>
<link href="https://fonts.googleapis.com/css2?family=Open+Sans:ital,wght@0,300;0,400;0,600;0,700;1,400&display=swap" rel="stylesheet">
<style>
:root{
  --red:#d8141c;
  --red-dark:#b30d14;
  --ink:#2b2b2b;
  --text:#555;
  --muted:#999;
  --line:#e2e2e2;
  --panel:#f1f1f1;
  --dark:#333335;
  --darker:#2a2a2c;
  --white:#fff;
}
*{box-sizing:border-box;margin:0;padding:0}
html,body{width:1200px;height:2400px;overflow:hidden}
body{position:relative;background:var(--white);font-family:"Open Sans",Arial,sans-serif;color:var(--text)}
.abs{position:absolute}

/* header */
.top-rule{left:0;top:0;width:1200px;height:5px;background:var(--red)}
.site-header{left:0;top:5px;width:1200px;height:173px;background:var(--white)}
.club-mark{left:125px;top:30px;width:126px;height:126px;border-radius:50%;background:var(--red)}
.site-title{left:312px;top:40px;font-size:38px;font-weight:600;letter-spacing:1px;color:var(--red)}
.site-title span{color:var(--ink)}
.main-nav{left:300px;top:112px;width:800px;height:44px;border-top:1px solid var(--line);border-bottom:1px solid var(--line);display:flex;align-items:center;padding-left:10px}
.main-nav a{font-size:15px;color:var(--ink);text-decoration:none;margin-right:28px;letter-spacing:.3px;line-height:42px}
.main-nav a.is-active{color:var(--red);border-top:3px solid var(--red);line-height:36px;margin-top:-3px}
.nav-search{left:1050px;top:125px}

/* hero */
.hero{left:0;top:178px;width:1200px;height:400px;border-bottom:6px solid var(--red);background:linear-gradient(90deg,#3a3a3a 0%,#4a4a4a 25%,#262626 55%,#1e1e1e 100%)}
.hero-photo{left:0;top:0;width:600px;height:394px;background:radial-gradient(ellipse at 40% 45%,#6a6a6a 0%,#3c3c3c 55%,rgba(30,30,30,0) 100%)}
.hero-title{left:638px;top:82px;font-size:46px;font-weight:400;color:var(--white)}
.hero-sub{left:638px;top:150px;font-size:25px;font-style:italic;line-height:34px;color:var(--white)}
.hero-text{left:638px;top:226px;font-size:16px;line-height:26px;color:#e8e8e8}
.hero-btn{left:638px;top:280px;width:142px;height:36px;border:2px solid var(--white);color:var(--white);font-size:15px;font-weight:600;text-align:center;line-height:32px}
.hero-dots{left:960px;top:360px;display:flex;gap:8px}
.hero-dots i{display:block;width:12px;height:12px;border-radius:50%;background:#777}
.hero-dots i.on{background:var(--red)}

/* content */
.section-head{font-size:38px;font-weight:300;color:var(--ink);letter-spacing:.5px}
.head-rule{height:2px;background:var(--line)}
.head-rule::before{content:"";display:block;width:60px;height:2px;background:var(--red)}
.archive-link{left:640px;top:646px;font-size:14px;color:var(--muted);font-style:italic}
.post-title{font-size:28px;font-weight:400;color:var(--ink)}
.post-image{border:6px solid #efefef}
.post-text{font-size:15px;line-height:24px;color:var(--text);border-left:2px solid var(--line);padding-left:14px;width:560px}
.post-text b{color:var(--ink)}
.read-more{font-size:14px;color:var(--ink)}
.read-more::before{content:"\25B8";color:var(--red);margin-right:6px}
.post-divider{height:2px;width:560px;background:var(--line)}
.post-divider::before{content:"";display:block;width:60px;height:2px;background:var(--red)}

/* side promos */
.promo-register{left:768px;top:715px;width:302px;height:204px;background:linear-gradient(135deg,#f4f4f4,#d9d9d9)}
.promo-register .big{position:absolute;left:22px;font-size:50px;font-weight:300;line-height:54px;letter-spacing:1px}
.promo-register .season{position:absolute;left:24px;top:124px;font-size:17px;font-weight:700;color:var(--ink)}
.promo-register .bar{position:absolute;left:0;bottom:0;width:100%;height:40px;background:#1c1c1c;color:var(--red);font-weight:700;font-size:18px;line-height:40px;padding-left:24px}
.promo-sign{left:770px;top:950px;width:300px;height:222px;background:var(--white);border:6px solid var(--red-dark);border-radius:14px;box-shadow:0 0 0 3px #ddd}
.promo-referee{left:768px;top:1200px;width:302px;height:494px;background:linear-gradient(180deg,#f3f3f3,#cfcfcf);text-align:center}
.promo-referee .l1{margin-top:16px;font-size:44px;font-weight:400;color:var(--ink);line-height:52px}
.promo-referee .l2{font-size:56px;font-weight:400;color:var(--red);line-height:62px}
.ball{width:210px;height:210px;border-radius:50%;margin:14px auto 0;background:radial-gradient(circle at 38% 35%,#ffffff 0%,#e6e6e6 45%,#555 100%)}
.promo-referee .season{margin-top:18px;font-size:22px;font-weight:600;color:var(--ink)}
.promo-referee .info{margin:8px auto 0;width:240px;font-size:15px;line-height:20px;color:var(--text)}
.promo-referee .more{margin-top:6px;font-size:18px;font-weight:700;color:var(--red)}

/* sponsors */
.sponsor-band{left:0;top:1754px;width:1200px;height:84px;background:var(--dark)}
.sponsor-title{left:0;top:1772px;width:1200px;text-align:center;font-size:34px;font-weight:400;color:var(--white)}
.sponsor-title b{font-weight:700}
.sponsor-strip{left:0;top:1838px;width:1200px;height:135px;background:#e4e4e4}
.sponsor{top:1866px;width:184px;height:82px;background:var(--white);display:flex;align-items:center;justify-content:center;font-size:19px;font-weight:700;color:var(--ink);box-shadow:0 1px 3px rgba(0,0,0,.15)}
.red-band{left:0;top:1973px;width:1200px;height:19px;background:var(--red)}

/* footer */
.site-footer{left:0;top:1992px;width:1200px;height:384px;background:var(--darker)}
.foot-head{top:2036px;font-size:26px;font-weight:400;color:var(--white);letter-spacing:.5px}
.foot-rule{top:2078px;height:2px;background:#4a4a4c}
.foot-list{list-style:none;font-size:13px;color:#ddd}
.foot-list li{height:30px;line-height:30px}
.foot-list li::before{content:"\25B8";color:var(--red);font-size:11px;margin-right:8px}
.fix-list li{border-bottom:1px dotted #555;width:150px}
.foot-badge{left:130px;top:2237px;width:64px;height:64px;border-radius:50%;background:#9a9a9a}
.foot-address{left:228px;top:2240px;font-size:13px;line-height:18px;color:#ddd}
.foot-address b{font-size:15px;color:var(--white)}
.copyright{left:0;top:2376px;width:1200px;height:24px;background:#232325;color:#888;font-size:12px;text-align:center;line-height:24px}
</style>
</head>
<body>

<div class="abs top-rule"></div>
<header class="abs site-header">
  <div class="abs club-mark" aria-hidden="true"></div>
  <div class="abs site-title">KENWICK <span>FC</span></div>
  <nav class="abs main-nav">
    <a>HOME</a><a>NEWS</a><a>FIXTURE &amp; RESULTS</a><a>PHOTO GALLERY</a><a class="is-active">SPONSOR CLUB</a><a>CONTACT US</a>
  </nav>
  <svg class="abs nav-search" width="18" height="18" viewBox="0 0 18 18" aria-label="Search"><circle cx="7" cy="7" r="5.5" fill="none" stroke="#2b2b2b" stroke-width="2"/><line x1="11" y1="11" x2="16.5" y2="16.5" stroke="#2b2b2b" stroke-width="2.4"/></svg>
</header>

<section class="abs hero">
  <div class="abs hero-photo" role="img" aria-label="Footballer in red kit leaping to volley a ball against a dark stormy sky"></div>
  <h1 class="abs hero-title">HBJCA Charity Day</h1>
  <p class="abs hero-sub">Charity Day Sunday 16th march 2014,<br>11Am Kick Off</p>
  <p class="abs hero-text">Come and enjoy a fun family day whilst supporting<br>The Children's Hospital at Northvale</p>
  <div class="abs hero-btn">LEARN MORE</div>
  <div class="abs hero-dots"><i class="on"></i><i></i><i></i><i></i><i></i><i></i></div>
</section>

<!-- latest news -->
<h2 class="abs section-head" style="left:130px;top:606px">LATEST NEWS</h2>
<div class="abs archive-link">Archive</div>
<div class="abs head-rule" style="left:130px;top:664px;width:560px"></div>

<h3 class="abs post-title" style="left:130px;top:695px">Information night</h3>
<div class="abs post-image" style="left:130px;top:751px;width:560px;height:174px;background:linear-gradient(135deg,#c81a20,#8e0f14 60%,#5a5a5a)" role="img" aria-label="Close-up of a club medal resting on a red team shirt"></div>
<p class="abs post-text" style="left:130px;top:941px">To Parents and players, Kenwick FC will be holding an information night for Parents on the following nights:Under 6 – 11 - 5th march at 6:00pm and Under 12 - 16 - 6th March at 6:00pm.</p>
<div class="abs read-more" style="left:130px;top:1028px">Read more</div>
<div class="abs post-divider" style="left:130px;top:1080px"></div>

<h3 class="abs post-title" style="left:130px;top:1110px">Registration</h3>
<p class="abs post-text" style="left:130px;top:1164px">We have two last days for registration as teams are filling up quickly. <b>Wednesday 19th and 20th Thursday February at Kenwick Central Bowling Club 6pm- 8.30pm.</b></p>
<div class="abs read-more" style="left:130px;top:1240px">Read more</div>
<div class="abs post-divider" style="left:130px;top:1296px"></div>

<h3 class="abs post-title" style="left:130px;top:1326px">2014 registration</h3>
<div class="abs post-image" style="left:130px;top:1380px;width:560px;height:180px;background:linear-gradient(180deg,#d9d9d9,#f2f2f2 40%,#c9c9c9)" role="img" aria-label="Junior players in red and white kit celebrating with their coach"></div>
<p class="abs post-text" style="left:130px;top:1580px">Registrations are now open online, registrations nights are On the 22nd , 23rd, 29 &amp; 30th january 6pm-8.30pm all nights in Kenwick Central Bowling Club Main entrance - room to the left.</p>
<div class="abs read-more" style="left:130px;top:1658px">Read more</div>

<!-- registration -->
<h2 class="abs section-head" style="left:768px;top:606px">REGISTRATION</h2>
<div class="abs head-rule" style="left:768px;top:664px;width:302px"></div>

<div class="abs promo-register">
  <div class="big" style="top:16px;color:#555">REGISTER</div>
  <div class="big" style="top:66px;color:var(--red)">ONLINE</div>
  <div class="season">2014 SEASON</div>
  <div class="bar">CLICK HERE</div>
</div>

<div class="abs promo-sign">
  <svg width="288" height="210" viewBox="0 0 288 210" aria-label="No smoking">
    <text x="18" y="100" font-family="Open Sans, sans-serif" font-weight="700" font-size="92" fill="#1a1a1a">NO</text>
    <g transform="translate(210,62)">
      <circle r="46" fill="#fff" stroke="#c8141b" stroke-width="9"/>
      <rect x="-34" y="-6" width="56" height="12" fill="#1a1a1a"/>
      <rect x="22" y="-6" width="10" height="12" fill="#1a1a1a"/>
      <line x1="-32" y1="-32" x2="32" y2="32" stroke="#c8141b" stroke-width="9"/>
    </g>
    <rect x="14" y="124" width="260" height="4" fill="#1a1a1a"/>
    <text x="144" y="188" text-anchor="middle" font-family="Open Sans, sans-serif" font-weight="700" font-size="52" fill="#1a1a1a">SMOKING</text>
  </svg>
</div>

<div class="abs promo-referee">
  <div class="l1">BECOME A</div>
  <div class="l2">REFEREE</div>
  <div class="ball" role="img" aria-label="Black and white football"></div>
  <div class="season">2014 SEASON</div>
  <div class="info">Find out how to become a referee for the new 2013 season</div>
  <div class="more">READ MORE</div>
</div>

<!-- sponsors -->
<div class="abs sponsor-band"></div>
<svg class="abs" style="left:127px;top:1773px" width="46" height="46" viewBox="0 0 46 46" aria-label="Previous"><circle cx="23" cy="23" r="21" fill="none" stroke="#fff" stroke-width="2"/><path d="M27 13 L17 23 L27 33 M17 23 H33" fill="none" stroke="#fff" stroke-width="2.5"/></svg>
<h2 class="abs sponsor-title">Kenwick <b>FC</b> Sponsor's</h2>
<svg class="abs" style="left:1024px;top:1773px" width="46" height="46" viewBox="0 0 46 46" aria-label="Next"><circle cx="23" cy="23" r="21" fill="none" stroke="#fff" stroke-width="2"/><path d="M19 13 L29 23 L19 33 M29 23 H13" fill="none" stroke="#fff" stroke-width="2.5"/></svg>
<div class="abs sponsor-strip"></div>
<div class="abs sponsor" style="left:130px">Brightline Tec</div>
<div class="abs sponsor" style="left:384px">Mediaworks Hub</div>
<div class="abs sponsor" style="left:643px">Harlow &amp; Co</div>
<div class="abs sponsor" style="left:886px">Eastfield Trophies</div>
<div class="abs red-band"></div>

<!-- footer -->
<footer class="abs site-footer"></footer>
<div class="abs foot-head" style="left:130px">HOME</div>
<div class="abs foot-head" style="left:283px">CLUB</div>
<div class="abs foot-head" style="left:442px">FIXTURES &amp; RESULTS</div>
<div class="abs foot-rule" style="left:130px;width:116px"></div>
<div class="abs foot-rule" style="left:283px;width:116px"></div>
<div class="abs foot-rule" style="left:442px;width:656px"></div>

<ul class="abs foot-list" style="left:136px;top:2088px"><li>News</li><li>Gallery</li><li>Sponsor</li><li>Contact Us</li></ul>
<ul class="abs foot-list" style="left:293px;top:2088px"><li>History</li><li>Committee</li><li>Awards</li><li>Forms</li></ul>

<ul class="abs foot-list fix-list" style="left:452px;top:2088px"><li>Premier League</li><li>Premier League Res</li><li>Super League</li><li>Super League Res</li><li>Under 16 / 2</li><li>Under 17 / 1</li><li>Under 10 / 2</li><li>Under 10 / 3</li></ul>
<ul class="abs foot-list fix-list" style="left:615px;top:2088px"><li>Under 11 / 1</li><li>Under 12 / 3</li><li>Under 13 / 3</li><li>Under 14 / 3</li><li>AA Men / 5</li><li>AA Men / 6</li><li>AA Men / 8</li><li>AA Men / 10</li></ul>
<ul class="abs foot-list fix-list" style="left:778px;top:2088px"><li>AA Men / 10</li><li>AA Men / 14</li><li>07 ECL / Red</li><li>07 ECL / Green</li><li>08 ECL / Blue</li><li>08 ECL / Blue</li><li>08 ECL / Green</li><li>09 / Green</li></ul>
<ul class="abs foot-list fix-list" style="left:941px;top:2088px"><li>06 / A Green</li><li>06 / B Blue</li><li>06 / C Red</li><li>06 / D Purple</li><li>06 / E White</li><li>06 / F Brown</li></ul>

<div class="abs foot-badge" aria-hidden="true"></div>
<div class="abs foot-address"><b>Kenwick FC</b><br>48 Marlow St<br>Kenwick NSW 2290<br>Sydney, Australia</div>

<div class="abs copyright">Kenwick FC 2014</div>

</body>
</html>
```